Emergency Medical Training and Events Company Business Needs Business Card Design

We are in need of a business card for our dynamic company expanding its customer base and need to be easily contacted and identified for when we visit with government officials, potential EMS / Fire agencies and county coordinators to arrange for training programs for first responders to better prepare them for critical thinking at critical incidents.

Target Market(s)

EMS/Fire and Event Promoters

Industry/Entity Type

Medical

Contact Information for Business Card

Two cards, comparable designs:

Martin K. Halvey, Principal, m.halvey@rvqtlo.com
Owen Tash, Event and Training Specialist, o.tash@rvqtlo.com

Font styles to use
Other font styles liked:
• Cambria

Colors

Designer to choose colors to be used in the design.

Requirements
Must have
• Company Logo, Spots for Name, Title, Phone Number, Email, Website
• A bullet list stating that we offer, QRB CPR and First Aid Instructors, Hold the Line Instructors, Event EMS, CME's, MCI Training and Planning. We prefer to have a black background for the card but if you can make a blue or white card stand out we would review that as well.
Should not have
• Tacky logos or special sayings ... simple, elegant, professional is the look we seek

```html
<!DOCTYPE html>
<html lang="en">
<head>
<meta charset="utf-8">
<title>R.V.Q. Solutions of TLO – Business Card</title>
<link rel="stylesheet" href="https://fonts.googleapis.com/css2?family=Lato:wght@400;700&display=swap">
<style>
  :root {
    --page-bg: #dcdde1;
    --card-deep: #07124a;
    --card-light: #11266b;
    --accent-red: #d3232a;
    --text-white: #f2f3f7;
    --text-soft: #e3e6f0;
  }
  * { margin: 0; padding: 0; box-sizing: border-box; }
  html, body {
    width: 1200px;
    height: 800px;
    overflow: hidden;
    background: var(--page-bg);
    font-family: "Lato", sans-serif;
  }
  .canvas { position: relative; width: 1200px; height: 800px; }

  .card {
    position: absolute;
    background: linear-gradient(60deg, var(--card-deep) 0%, var(--card-light) 100%);
    color: var(--text-white);
  }
  .card--front { left: 346px; top: 102px; width: 488px; height: 278px; }
  .card--back  { left: 355px; top: 427px; width: 471px; height: 270px; }

  .brand {
    position: absolute;
    display: flex;
    align-items: center;
    gap: 10px;
    white-space: nowrap;
  }
  .brand__dot {
    flex: none;
    border-radius: 50%;
    background: var(--accent-red);
  }
  .brand__name {
    font-weight: 700;
    color: var(--text-white);
    letter-spacing: 0.2px;
  }
  .card--front .brand { left: 0; right: 0; top: 118px; justify-content: center; }
  .card--front .brand__dot { width: 34px; height: 34px; }
  .card--front .brand__name { font-size: 24px; }

  .card--back .brand { left: 44px; top: 119px; }
  .card--back .brand__dot { width: 26px; height: 26px; }
  .card--back .brand__name { font-size: 16px; }

  .services {
    position: absolute;
    left: 0; right: 0; top: 220px;
    text-align: center;
    font-size: 13.5px;
    line-height: 18px;
    color: var(--text-soft);
    list-style: none;
  }
  .services__row { display: block; }
  .services__item { display: inline; margin: 0 3px; }
  .services__item::before {
    content: "";
    display: inline-block;
    width: 5px; height: 5px;
    margin-right: 4px;
    border-radius: 50%;
    background: var(--accent-red);
    vertical-align: 2px;
  }

  .contact-divider {
    position: absolute;
    left: 267px; top: 77px;
    width: 1px; height: 115px;
    background: var(--accent-red);
  }
  .contact {
    position: absolute;
    left: 283px; top: 73px;
  }
  .contact__name {
    font-size: 18.5px;
    font-weight: 700;
    color: var(--accent-red);
    line-height: 22px;
  }
  .contact__title {
    font-size: 12.5px;
    color: var(--text-soft);
    margin-top: 2px;
  }
  .contact__list {
    list-style: none;
    margin-top: 17px;
    font-size: 13px;
    line-height: 16.5px;
    color: var(--text-soft);
  }
  .contact__item { display: flex; align-items: center; gap: 4px; }
  .contact__icon { width: 9px; height: 9px; flex: none; fill: var(--accent-red); }
</style>
</head>
<body>
<main class="canvas">

  <section class="card card--front" aria-label="Card front">
    <div class="brand">
      <span class="brand__dot"></span>
      <span class="brand__name">R.V.Q. Solutions of TLO</span>
    </div>
    <ul class="services">
      <li class="services__row">
        <span class="services__item">QRB CPR</span>
        <span class="services__item">First Aid Instructors,</span>
        <span class="services__item">Hold the Line Instructors</span>
      </li>
      <li class="services__row">
        <span class="services__item">EMS,</span>
        <span class="services__item">CME's,</span>
        <span class="services__item">MCI Training and Planning</span>
      </li>
    </ul>
  </section>

  <section class="card card--back" aria-label="Card back">
    <div class="brand">
      <span class="brand__dot"></span>
      <span class="brand__name">R.V.Q. Solutions of TLO</span>
    </div>
    <div class="contact-divider"></div>
    <div class="contact">
      <p class="contact__name">Martin K. Halvey</p>
      <p class="contact__title">Principal</p>
      <ul class="contact__list">
        <li class="contact__item">
          <svg class="contact__icon" viewBox="0 0 10 10" aria-hidden="true"><path d="M2 0.5 L3.6 0.5 L4.3 2.8 L3.2 3.8 Q4.2 5.9 6.2 6.8 L7.2 5.7 L9.5 6.4 L9.5 8 Q9.5 9.5 8 9.5 Q0.5 9 0.5 2 Q0.5 0.5 2 0.5 Z"/></svg>
          555.014.2002
        </li>
        <li class="contact__item">
          <svg class="contact__icon" viewBox="0 0 10 10" aria-hidden="true"><path d="M2.5 0 H7.5 V10 H2.5 Z M3.3 0.9 V8.4 H6.7 V0.9 Z"/></svg>
          555.019.7890
        </li>
        <li class="contact__item">
          <svg class="contact__icon" viewBox="0 0 10 10" aria-hidden="true"><path d="M0 2 H10 V8.5 H0 Z M0.6 2.4 L5 5.6 L9.4 2.4 Z" fill-rule="evenodd"/></svg>
          m.halvey@rvqtlo.com
        </li>
        <li class="contact__item">
          <svg class="contact__icon" viewBox="0 0 10 10" aria-hidden="true"><circle cx="5" cy="5" r="4.3" fill="none" stroke="#d3232a" stroke-width="0.9"/><path d="M0.7 5 H9.3 M5 0.7 V9.3" stroke="#d3232a" stroke-width="0.8"/><ellipse cx="5" cy="5" rx="2" ry="4.3" fill="none" stroke="#d3232a" stroke-width="0.8"/></svg>
          www.rvqtlo.com
        </li>
      </ul>
    </div>
  </section>

</main>
</body>
</html>
```